Tarvil GmbH business card

We Tarvil GmbH based in Switzerland are looking for a business card design. The Fresh Jung, appealing to customers of all kinds. We already have a logo to upload but still a business card. Details: Tarvil GmbH Address: Lindenweg 14b in 9412 Rudolfen. Tel: 41 76 392 00 47, web: Tarvil.ch, E-mail: info@Tarvil.ch Facebook: Tarvil GmbH. I am the Managing Director: Lukas Verholt. On reverse: Title: Transporter and bus rental Gross: Without deposit Super prices
Contact Information for Business Card
Siehe Projektbeschreibung
Requirements
Should not have
- Other pictures

```html
<!DOCTYPE html>
<html lang="de">
<head>
<meta charset="utf-8">
<title>Tarvil GmbH – Visitenkarte</title>
<link rel="stylesheet" href="https://fonts.googleapis.com/css2?family=Open+Sans:wght@400;600&family=Barlow+Semi+Condensed:wght@600&display=swap">
<style>
  :root {
    --stage: #3a332f;
    --card-blue: #1b1d78;
    --card-white: #ffffff;
    --ink-navy: #1d2383;
    --ink-grey: #4a4a4a;
    --ink-steel: #7f93b3;
    --front-text: #c9cede;
    --rule: #c8c8c8;
  }
  * { box-sizing: border-box; margin: 0; padding: 0; }
  html, body {
    width: 1200px; height: 769px; overflow: hidden;
    background: var(--stage);
  }
  .canvas {
    position: relative; width: 1200px; height: 769px;
    display: flex; align-items: center; justify-content: center; gap: 40px;
  }
  .card {
    width: 540px; height: 309px; position: relative;
    box-shadow: 0 10px 30px rgba(0,0,0,.45);
  }

  /* Front side */
  .card--front {
    background: var(--card-blue);
    color: var(--front-text);
    font-family: "Open Sans", sans-serif;
    display: flex; flex-direction: column; align-items: center; justify-content: center;
  }
  .front__brand {
    display: flex; align-items: center; gap: 12px;
    font-size: 40px; font-weight: 600; letter-spacing: 1px; color: var(--front-text);
    margin-bottom: 18px;
  }
  .front__mark { width: 22px; height: 22px; border-radius: 50%; background: var(--front-text); }
  .front__service { font-size: 14px; margin-left: 60px; }
  .front__claim { font-size: 28px; font-weight: 600; line-height: 1.1; }
  .front__claim span { font-size: 18px; font-weight: 400; }

  /* Back side */
  .card--back {
    background: var(--card-white);
    display: flex; align-items: center;
    padding: 0 34px;
  }
  .back__brand {
    flex: 1; display: flex; align-items: center; gap: 12px;
    font-family: "Open Sans", sans-serif;
    font-size: 34px; font-weight: 600; letter-spacing: 2px; color: var(--ink-navy);
  }
  .back__mark { width: 18px; height: 18px; background: var(--ink-navy); }
  .back__rule { width: 1px; height: 180px; background: var(--rule); margin: 0 22px; }
  .back__contact { width: 205px; font-family: "Open Sans", sans-serif; color: var(--ink-grey); font-size: 14px; line-height: 1.35; }
  .contact__name {
    font-family: "Barlow Semi Condensed", sans-serif; font-weight: 600;
    font-size: 21px; color: var(--ink-navy); letter-spacing: .5px; line-height: 1;
  }
  .contact__role { color: var(--ink-steel); font-size: 14px; margin-bottom: 10px; }
  .contact__address { margin-bottom: 6px; }
  .contact__line { display: flex; align-items: center; gap: 8px; }
  .contact__line svg { width: 13px; height: 13px; fill: var(--ink-navy); flex: none; }
</style>
</head>
<body>
<main class="canvas">
  <section class="card card--front" aria-label="Vorderseite">
    <div class="front__brand"><span class="front__mark"></span>Tarvil</div>
    <p class="front__service">Transporter und Bus Vermietung</p>
    <p class="front__claim">Ohne Kaution <span>Super Preise</span></p>
  </section>

  <section class="card card--back" aria-label="Rückseite">
    <div class="back__brand"><span class="back__mark"></span>TARVIL</div>
    <div class="back__rule"></div>
    <div class="back__contact">
      <p class="contact__name">LUKAS VERHOLT</p>
      <p class="contact__role">Manager</p>
      <p class="contact__address">Lindenweg 14b in 9412 Rudolfen.</p>
      <p class="contact__line">
        <svg viewBox="0 0 24 24"><path d="M6.6 10.8a15 15 0 0 0 6.6 6.6l2.2-2.2a1 1 0 0 1 1-.25 11.4 11.4 0 0 0 3.6.57 1 1 0 0 1 1 1V20a1 1 0 0 1-1 1A17 17 0 0 1 3 4a1 1 0 0 1 1-1h3.5a1 1 0 0 1 1 1c0 1.25.2 2.45.57 3.57a1 1 0 0 1-.25 1z"/></svg>
        +41 76 392 00 47
      </p>
      <p class="contact__line">
        <svg viewBox="0 0 24 24"><path d="M2 5h20v14H2z M3.5 6.5 12 13l8.5-6.5" fill="none" stroke="#1d2383" stroke-width="2"/></svg>
        info@Tarvil.ch
      </p>
      <p class="contact__line">
        <svg viewBox="0 0 24 24"><circle cx="12" cy="12" r="10"/><path d="M2 12h20M12 2a15 15 0 0 1 0 20M12 2a15 15 0 0 0 0 20" fill="none" stroke="#fff" stroke-width="1.5"/></svg>
        Tarvil.ch
      </p>
    </div>
  </section>
</main>
</body>
</html>
```